Redesign the *Settings* screen for the BrelloZ app.

BrelloZ app is in production, but we need to refresh and redesign the settings screen to be cleaner, easier, more intuitive, and more professional looking.

Project Deadline Extended
Reason: Several designers have requested more time. This will also give time to provide feedback on existing designs.

Requirements
Must have
• Black background, so that the screen is consistent with the rest of the app.

```html
<!DOCTYPE html>
<html lang="en">
<head>
<meta charset="utf-8">
<title>BrelloZ Settings</title>
<link href="https://fonts.googleapis.com/css2?family=Roboto:wght@300;400;500;700&display=swap" rel="stylesheet">
<style>
:root{
  --page:#111111;
  --status:#1c1c1c;
  --row:#0b0b0b;
  --divider:#262626;
  --ink:#f1f1f1;
  --icon:#e6e6e6;
  --outline:#9a9a9a;
  --muted:#8a8a8a;
  --red:#c0282e;
  --link:#e0383e;
  --info-bg:#e9e9e9;
  --info-ink:#111111;
  --footer:#161616;
}
*{box-sizing:border-box;margin:0;padding:0}
html,body{width:1200px;height:1200px;overflow:hidden;background:var(--page)}
body{position:relative;font-family:"Roboto",Helvetica,Arial,sans-serif;color:var(--ink)}
.screen{position:absolute;left:266px;top:5px;width:522px;height:930px;background:var(--row);transform:scale(1.28);transform-origin:0 0;overflow:hidden}
.status-bar{height:37px;background:var(--status);color:#fff;font-size:15px;display:flex;align-items:center;justify-content:space-between;padding:0 12px}
.status-bar .carrier{display:flex;align-items:center;gap:4px}
.status-bar .right{display:flex;align-items:center;gap:6px}
.battery{width:32px;height:13px;border:1px solid #fff;border-radius:3px;padding:1px}
.battery::before{content:"";display:block;height:100%;background:#fff;border-radius:1px}
.setting{height:82.5px;border-bottom:1px solid var(--divider);display:flex;align-items:center;justify-content:space-between;padding:0 11px}
.setting .label{font-size:20px}
.options{display:flex;align-items:center;gap:17px}
.opt{width:40px;height:40px;border-radius:50%;border:1px solid var(--outline);display:flex;align-items:center;justify-content:center;color:var(--icon);font-size:12px;font-weight:500}
.opt.active{background:var(--red);border-color:var(--red);color:#fff}
.opt svg{width:20px;height:20px}
.opt svg.arrow{width:18px;height:18px}
.info{width:26px;height:26px;border-radius:50%;background:var(--info-bg);color:var(--info-ink);font-family:Georgia,serif;font-weight:700;font-size:15px;display:flex;align-items:center;justify-content:center;margin-left:-4px}
.value{color:var(--link);font-size:20px;font-weight:700}
.link{height:54px;border-bottom:1px solid var(--divider);display:flex;align-items:center;justify-content:space-between;padding:0 11px;color:var(--link);font-size:18px}
.link .chev{color:#777;font-size:20px;font-weight:300}
.version{height:30px;background:var(--footer);color:var(--muted);font-size:12px;display:flex;align-items:center;justify-content:center}
.tab-bar{height:70px;background:var(--row);display:flex;border-top:1px solid var(--divider)}
.tab{flex:1;display:flex;flex-direction:column;align-items:center;justify-content:center;gap:4px;font-size:10px;font-weight:500;color:var(--icon)}
.tab svg{width:36px;height:36px}
.tab.current{color:var(--link)}
</style>
</head>
<body>
<main class="screen">
  <div class="status-bar">
    <span class="carrier">●●●○○ VERA
      <svg width="18" height="12" viewBox="0 0 18 12" fill="none" stroke="#fff" stroke-width="2"><path d="M1 4a11 11 0 0 1 16 0M4 7a7 7 0 0 1 10 0"/><circle cx="9" cy="10" r="1.3" fill="#fff" stroke="none"/></svg>
    </span>
    <span>4:21 PM</span>
    <span class="right">
      <svg width="10" height="16" viewBox="0 0 10 16" fill="none" stroke="#888" stroke-width="1.3"><path d="M1 4l8 8-4 3V1l4 3-8 8"/></svg>
      100% <span class="battery"></span>
    </span>
  </div>

  <div class="setting"><span class="label">Pistol</span>
    <div class="options">
      <span class="opt active"><svg viewBox="0 0 20 20" fill="#fff"><path d="M2 6h15v4H9l-1 5H5l1-5H2z"/></svg></span>
      <span class="opt"><svg viewBox="0 0 20 20" fill="#e6e6e6"><path d="M1 9h18v1.5H12l-1 3H9.5l.5-3H6l-1 2H3.5l.5-2H1z"/></svg></span>
    </div>
  </div>

  <div class="setting"><span class="label">Current Firearm</span><span class="value">K340</span></div>

  <div class="setting"><span class="label">Right Handed</span>
    <div class="options">
      <span class="opt"><svg viewBox="0 0 20 20" fill="#e6e6e6"><path d="M5 9V4a1 1 0 0 1 2 0v5V2.5a1 1 0 0 1 2 0V9V3a1 1 0 0 1 2 0v6V4.5a1 1 0 0 1 2 0V12l1.5-2.5a1 1 0 0 1 1.7 1L14 16a4 4 0 0 1-4 3H9a4 4 0 0 1-4-4z"/></svg></span>
      <span class="opt active"><svg viewBox="0 0 20 20" fill="#fff"><path d="M15 9V4a1 1 0 0 0-2 0v5V2.5a1 1 0 0 0-2 0V9V3a1 1 0 0 0-2 0v6V4.5a1 1 0 0 0-2 0V12L5.5 9.5a1 1 0 0 0-1.7 1L6 16a4 4 0 0 0 4 3h1a4 4 0 0 0 4-4z"/></svg></span>
    </div>
  </div>

  <div class="setting"><span class="label">Dry Practice</span>
    <div class="options">
      <span class="opt"><svg viewBox="0 0 20 20" fill="#e6e6e6"><path d="M7 17V8c0-3 1.5-5 3-6 1.5 1 3 3 3 6v9z"/><rect x="6" y="17" width="8" height="2"/></svg></span>
      <span class="opt active"><svg viewBox="0 0 20 20" fill="#fff"><rect x="8" y="1" width="4" height="13" rx="1"/><rect x="8" y="15.5" width="4" height="3"/></svg></span>
      <span class="opt">CO<sub style="font-size:8px">2</sub></span>
    </div>
  </div>

  <div class="setting"><span class="label">Device Mount Position</span>
    <div class="options">
      <span class="opt"><svg class="arrow" viewBox="0 0 18 18" fill="none" stroke="currentColor" stroke-width="1.4" stroke-linecap="round"><path d="M9 16V2M4 7l5-5 5 5"/></svg></span>
      <span class="opt active"><svg class="arrow" viewBox="0 0 18 18" fill="none" stroke="currentColor" stroke-width="1.4" stroke-linecap="round"><path d="M9 2v14M4 11l5 5 5-5"/></svg></span>
      <span class="info">i</span>
    </div>
  </div>

  <div class="setting"><span class="label">Device Mount Location</span>
    <div class="options">
      <span class="opt active"><svg class="arrow" viewBox="0 0 18 18" fill="none" stroke="currentColor" stroke-width="1.4" stroke-linecap="round"><path d="M9 2v14M4 11l5 5 5-5"/></svg></span>
      <span class="opt"><svg class="arrow" viewBox="0 0 18 18" fill="none" stroke="currentColor" stroke-width="1.4" stroke-linecap="round"><path d="M9 16V2M4 7l5-5 5 5"/></svg></span>
      <span class="opt"><svg class="arrow" viewBox="0 0 18 18" fill="none" stroke="currentColor" stroke-width="1.4" stroke-linecap="round"><path d="M16 9H2M7 4L2 9l5 5"/></svg></span>
      <span class="opt"><svg class="arrow" viewBox="0 0 18 18" fill="none" stroke="currentColor" stroke-width="1.4" stroke-linecap="round"><path d="M2 9h14M11 4l5 5-5 5"/></svg></span>
      <span class="info">i</span>
    </div>
  </div>

  <div class="setting"><span class="label">Bullseye Mode</span>
    <div class="options">
      <span class="opt active">OFF</span>
      <span class="opt">ON</span>
      <span class="info">i</span>
    </div>
  </div>

  <div class="link">Logout [jorin]<span class="chev">〉</span></div>
  <div class="link">Sync Account Data<span class="chev">〉</span></div>
  <div class="link">Disconnect Bluetooth<span class="chev">〉</span></div>
  <div class="link">Report Issue<span class="chev">〉</span></div>

  <div class="version">App Version: 2.3.9.05</div>

  <nav class="tab-bar">
    <div class="tab"><svg viewBox="0 0 36 36" fill="none" stroke="#e6e6e6" stroke-width="1.6"><circle cx="18" cy="18" r="14"/><circle cx="18" cy="18" r="9"/><circle cx="18" cy="18" r="4"/><path d="M18 1v8M18 27v8M1 18h8M27 18h8"/></svg>TRAIN</div>
    <div class="tab"><svg viewBox="0 0 36 36" fill="none" stroke="#e6e6e6" stroke-width="1.6"><rect x="4" y="18" width="7" height="15"/><rect x="15" y="4" width="7" height="29"/><rect x="26" y="12" width="7" height="21"/></svg>HISTORY</div>
    <div class="tab"><svg viewBox="0 0 36 36" fill="none" stroke="#e6e6e6" stroke-width="1.6"><path d="M2 11l16-6 16 6-16 6z"/><path d="M9 14v8c4 4 14 4 18 0v-8"/><path d="M30 12v12"/><circle cx="30" cy="26" r="1.5"/></svg>LEARN</div>
    <div class="tab current"><svg viewBox="0 0 36 36"><path fill="#e0383e" d="M15 2h6l1 5 4 2 4-3 4 4-3 4 2 4 5 1v6l-5 1-2 4 3 4-4 4-4-3-4 2-1 5h-6l-1-5-4-2-4 3-4-4 3-4-2-4-5-1v-6l5-1 2-4-3-4 4-4 4 3 4-2z" transform="scale(.9) translate(2 2)"/><circle cx="18" cy="18" r="5" fill="#0b0b0b"/></svg>SETTINGS</div>
  </nav>
</main>
</body>
</html>
```